Rapidly growing regional logistics company looking for a modern clean website design.

We need a website for a 5 year old company based in New England.
We offer a complete logistics solution. With services dedicated to the changing economic environment. Services to our customers include, same day delivery, trucking and van service, warehouse & storage, pool distribution, and B2B installations.
We've implemented leading technology along the way, that provides visibility, accountability, up to the minute tracking, and project management.
Our goal to be known in the industry we service as an excellent provider of time-critical services and dependability.
Independently of the services we offer, our customers know that they can count on a true partner.

Target Market(s)

B2B, including printers, retail, manufacturers, wholesalers, electronics, any company that needs product delivered or warehoused

Industry/Entity Type

Logistics

Coding

Coded - Design and coding required

Number of Pages Required

5+ page

Font styles to use
Sans Serif

Colors
0255a3

Requirements
Must have
• Clean, modern design, limited clutter. Limited tabs, preferred everything on 1st screen roll down to see info

```html
<!DOCTYPE html>
<html lang="en">
<head>
<meta charset="UTF-8">
<title>Harborline Logistics – Contact Us</title>
<link href="https://fonts.googleapis.com/css2?family=Raleway:wght@400;500;600&family=Jost:wght@400;500&display=swap" rel="stylesheet">
<style>
:root{
  --brand:#476fb6;
  --brand-dark:#3a5fa3;
  --ink:#2b2b2b;
  --line:#d4d4d4;
  --field:#cfcfcf;
  --white:#ffffff;
  --req:#e0262b;
  --hero-dark:#050608;
}
*{box-sizing:border-box;margin:0;padding:0}
html,body{width:1200px;height:1083px;overflow:hidden;background:var(--white)}
body{position:relative;font-family:"Jost",sans-serif;color:var(--ink)}
.abs{position:absolute;white-space:nowrap}

.topbar{left:0;top:0;width:1200px;height:38px;background:var(--brand);color:var(--white);font-size:15px}
.topbar-item{top:6px;display:flex;align-items:center;gap:9px}
.topbar-item .ring{width:27px;height:27px;border-radius:50%;background:var(--white);display:flex;align-items:center;justify-content:center;flex:none}

.header{left:0;top:38px;width:1200px;height:82px;background:var(--white)}
.brand{left:140px;display:flex;align-items:center;gap:8px}
.brand-dot{width:20px;height:20px;border-radius:50%;background:var(--brand);flex:none}
.brand-name{font-family:"Raleway",sans-serif;font-weight:500;font-size:19px;color:var(--brand);letter-spacing:.3px}

.nav{top:72px;font-family:"Raleway",sans-serif;font-size:14.5px;color:#333;letter-spacing:.2px}
.nav.active{color:var(--brand);font-weight:600}
.login{left:918px;top:62px;width:140px;height:34px;border-radius:17px;background:var(--brand);color:var(--white);font-family:"Raleway",sans-serif;font-weight:500;font-size:13.5px;letter-spacing:-.2px;display:flex;align-items:center;gap:7px;padding-left:2px}
.login .lock{width:30px;height:30px;border-radius:50%;border:1.5px solid var(--white);display:flex;align-items:center;justify-content:center;flex:none}

.hero{left:0;top:120px;width:1200px;height:328px;background:radial-gradient(ellipse at 42% 55%,#6b5a52 0%,#2a2220 30%,var(--hero-dark) 60%)}

.page-title{left:0;top:498px;width:1200px;text-align:center;font-family:"Raleway",sans-serif;font-size:32px;font-weight:400;color:var(--ink);letter-spacing:.3px}
.page-title span{color:var(--brand)}
.divider{top:556px;height:1px;background:linear-gradient(90deg,transparent,var(--line) 20%,var(--line))}
.divider.right{background:linear-gradient(90deg,var(--line),var(--line) 80%,transparent)}
.divider-mark{left:592px;top:548px;width:17px;height:17px;border-radius:50%;background:#777}

.section-heading{top:610px;font-family:"Raleway",sans-serif;font-size:24px;font-weight:400;color:#1e1e1e;letter-spacing:.2px}
.field{left:143px;width:424px;border:1px solid var(--field);border-radius:3px;font-size:12.5px;color:#333;padding:10px 10px}
.field i{font-style:normal;color:var(--req)}
.submit{left:142px;top:933px;width:112px;height:33px;border-radius:17px;background:var(--brand);color:var(--white);font-weight:500;font-size:16px;display:flex;align-items:center;justify-content:space-between;padding-left:14px;padding-right:2px}
.submit .dot{width:30px;height:30px;border-radius:50%;border:2px solid var(--white);background:var(--brand-dark)}
.col-rule{left:598px;top:615px;width:1px;height:365px;background:#e6e6e6}

.map{left:631px;top:667px;width:427px;height:155px;border:1px solid #bbb;background:linear-gradient(90deg,#e7e4dd 0%,#e9e6df 63%,#a4ccf7 65%,#a4ccf7 100%)}
.info-icon{left:631px;width:30px;height:30px;border-radius:50%;border:1.5px solid #2f3d5c;display:flex;align-items:center;justify-content:center}
.info-text{left:673px;font-size:13.5px;color:#222;line-height:21px}

.footer{left:0;top:1033px;width:1200px;height:50px;background:var(--brand);color:var(--white);font-size:12.5px}
.social{top:12px;width:27px;height:27px;border-radius:50%;border:1.5px solid var(--white)}
</style>
</head>
<body>

<div class="abs topbar">
  <div class="abs topbar-item" style="left:705px">
    <span class="ring"><svg width="14" height="10" viewBox="0 0 14 10"><rect x=".7" y=".7" width="12.6" height="8.6" fill="none" stroke="#476fb6" stroke-width="1.3"/><path d="M1 1l6 5 6-5" fill="none" stroke="#476fb6" stroke-width="1.3"/></svg></span>
    <span>info@harborline.com</span>
  </div>
  <div class="abs topbar-item" style="left:922px">
    <span class="ring"><svg width="14" height="14" viewBox="0 0 24 24"><path d="M6.6 10.8a15 15 0 006.6 6.6l2.2-2.2c.3-.3.7-.4 1-.2 1.1.4 2.3.6 3.6.6.6 0 1 .4 1 1V20c0 .6-.4 1-1 1A17 17 0 013 4c0-.6.4-1 1-1h3.5c.6 0 1 .4 1 1 0 1.3.2 2.5.6 3.6.1.3 0 .7-.2 1z" fill="#476fb6"/></svg></span>
    <span style="font-size:16px">555.014.2290</span>
  </div>
</div>

<header class="abs header">
  <div class="abs brand" style="top:36px">
    <span class="brand-dot"></span>
    <span class="brand-name">HARBORLINE LOGISTICS</span>
  </div>
</header>

<nav>
  <span class="abs nav" style="left:443px">HOME</span>
  <span class="abs nav" style="left:514px">ABOUT US</span>
  <span class="abs nav" style="left:616px">SERVICES</span>
  <span class="abs nav" style="left:713px;top:71px">CAREERS</span>
  <span class="abs nav active" style="left:807px;top:71px">CONTACT US</span>
  <span class="abs login">
    <span class="lock"><svg width="12" height="15" viewBox="0 0 12 15"><rect x="1" y="6" width="10" height="8" rx="1" fill="#fff"/><path d="M3 6V4a3 3 0 016 0v2" fill="none" stroke="#fff" stroke-width="1.6"/></svg></span>
    <span>CLIENT LOG-IN</span>
  </span>
</nav>

<div class="abs hero" role="img" aria-label="Photo of a hand touching glowing envelope, at-sign and phone contact icons on a dark background"></div>

<h1 class="abs page-title">CONTACT <span>US</span></h1>
<div class="abs divider" style="left:265px;width:315px"></div>
<div class="abs divider-mark"></div>
<div class="abs divider right" style="left:621px;width:315px"></div>

<h2 class="abs section-heading" style="left:143px">HOW CAN WE HELP YOU?</h2>
<form>
  <div class="abs field" style="top:667px;height:35px">Name <i>*</i></div>
  <div class="abs field" style="top:712px;height:35px">Email <i>*</i></div>
  <div class="abs field" style="top:756px;height:35px">Phone</div>
  <div class="abs field" style="top:801px;height:112px">Message <i>*</i></div>
  <div class="abs submit">SUBMIT <span class="dot"></span></div>
</form>

<div class="abs col-rule"></div>

<h2 class="abs section-heading" style="left:631px">HARBORLINE LOGISTICS</h2>
<div class="abs map" role="img" aria-label="Street map showing the office location near the waterfront"></div>

<div class="abs info-icon" style="top:846px"><svg width="12" height="16" viewBox="0 0 12 16"><path d="M6 1a5 5 0 015 5c0 4-5 9-5 9S1 10 1 6a5 5 0 015-5z" fill="#2f4a80"/><circle cx="6" cy="6" r="1.8" fill="#fff"/></svg></div>
<div class="abs info-text" style="top:843px">1180 Shoreline Rd Ste 4b Bayford,<br>RI 02899</div>

<div class="abs info-icon" style="top:895px"><svg width="14" height="14" viewBox="0 0 24 24"><path d="M6.6 10.8a15 15 0 006.6 6.6l2.2-2.2c.3-.3.7-.4 1-.2 1.1.4 2.3.6 3.6.6.6 0 1 .4 1 1V20c0 .6-.4 1-1 1A17 17 0 013 4c0-.6.4-1 1-1h3.5c.6 0 1 .4 1 1 0 1.3.2 2.5.6 3.6.1.3 0 .7-.2 1z" fill="#2f4a80"/></svg></div>
<div class="abs info-text" style="top:898px">(555)-014-7731</div>

<div class="abs info-icon" style="top:937px"><svg width="14" height="10" viewBox="0 0 14 10"><rect x=".7" y=".7" width="12.6" height="8.6" fill="#2f4a80"/><path d="M1 1l6 5 6-5" fill="none" stroke="#fff" stroke-width="1.2"/></svg></div>
<div class="abs info-text" style="top:940px">info@harborline.com</div>

<footer class="abs footer">
  <span class="abs" style="left:143px;top:17px">Copyright © 2017 Harborline Logistics . All Right Reserved.</span>
  <span class="abs" style="left:863px;top:15px;font-size:14px">Follow Us</span>
  <span class="abs social" style="left:931px" aria-label="Social profile"></span>
  <span class="abs social" style="left:963px" aria-label="Social profile"></span>
  <span class="abs social" style="left:995px" aria-label="Social profile"></span>
  <span class="abs social" style="left:1027px" aria-label="Social profile"></span>
</footer>

</body>
</html>
```